Talmero PSD Only - Joomla Web Design Project

We currently have a web page that need a revamp. We are a Telephony software and product company that serves medium to large corporations.

We have a focus on solutions and services and our goal with the new website is to be able to show sucess cases, white papers and have a web TV program to show our softwares working in real life to our clients.

We also need to get on chirpnet and PB. Some focus on veritcal markets are also important when designing the categories of our web site.

We currently have it published at www.talmero-example.com.br. This website MUST not be used for any reference of design. Any close images and proposals WILL NOT BE CONSIDER.

At this website you can find products names and services we offer are already there and could be used to be published in the new site.

We have attached our new Logo that needs to be used. Also MAKE SURE YOU USE he new colors that are presented on the new logo.
Updates

May I suggest you to use this Wordpress template as a suggestion. You can add modules and articles to it if you feel it is necessary.

Also, our focus will be on Custom Made Solutions. Products shall be only 50% of the priority.

Let's keep up with the good work.

Nilo

http://cms.layoutvault-example.com/wordpress_58104/

This is the template!

Please try to use light colors on the template (White space). The logo RGB colors can be used and the menu background would look good on blue (Same as logo) 

Reason: We made some changes on product logos and we will be updation the logos for the use on your jobs.

We have up-loaded the new logos for products and services that shall be used when presentation your work. Please use the new logos only. Any old logo from the current website will be dropped with no evaluation. Thanks

Please read the brief and use the new logos on your design. We also need costs for changing it to joomla. Please provide via email. nilo@talmero-example.com.br

Reason: We are waiting few more designs

Reason: We are still waiting for some inner pages

Target Market(s)

Any clients that need telecom products and services, software developers, banking and finance, government and health care industries

Industry/Entity Type

Software

Requirements
Must have
• Products, services and solution on the menu. A location for publishing videos on the home page.

Partners login and specific area for documents and other protected information.

Connection of Web learning and moodle (web training software)

Web chat

We also need an area that our clients could upload their phone consumption and we could do a simulation of what we could save in terms of phone expenses if they use our equipments and services. Such us consulting business made easy

Focus on our BRISK Platform which is our major software product and is custom made.
Nice to have
• - Flash images on the home
- Interactive forms so clients could assemble their own telecom solution for their needs. For example. PBX + CRM + Recording services + x number of phones + installation + maintenance
Should not have
• - Bold colors
- Too much text

```html
<!DOCTYPE html>
<html lang="en">
<head>
<meta charset="utf-8">
<title>Talmero – Home</title>
<link rel="stylesheet" href="https://fonts.googleapis.com/css2?family=Lato:wght@400;700&family=Open+Sans:ital,wght@0,400;0,600;0,700;1,400&display=swap">
<style>
:root{
  --blue:#1d4f9f;
  --blue-dark:#163f86;
  --blue-light:#2f86d6;
  --orange:#f08a1c;
  --orange-dark:#e06d0c;
  --text:#444;
  --muted:#6d6d6d;
  --line:#e2e2e2;
  --footer:#eeeeee;
  --hero-a:#eef1f5;
  --hero-b:#dfe5ec;
}
*{box-sizing:border-box;margin:0;padding:0}
html,body{width:690px;height:1200px;overflow:hidden;background:#fff}
body{position:relative;font-family:"Open Sans",Arial,sans-serif;color:var(--text);font-size:7.5px;line-height:1.4}
.abs{position:absolute}
a{color:var(--blue);text-decoration:none}
h2{font-family:"Lato",Arial,sans-serif;font-weight:700;color:var(--blue);font-size:14px;position:absolute}

/* header */
.header{position:absolute;left:0;top:0;width:690px;height:51px;background:linear-gradient(#fff,#f3f3f3)}
.brand{left:92px;top:16px;display:flex;align-items:center;gap:6px}
.brand-mark{width:18px;height:18px;background:var(--blue)}
.brand-name{font-family:"Open Sans",sans-serif;font-weight:700;font-size:15px;color:var(--blue);letter-spacing:2px}
.toolbar{left:470px;top:0;width:128px;height:17px;background:#e9e9e9;border:1px solid #d7d7d7;border-top:0;border-radius:0 0 3px 3px;display:flex;justify-content:space-around;align-items:center;font-size:6.5px;color:#777}
.toolbar span::before{content:"";display:inline-block;width:6px;height:6px;border-radius:50%;background:#aaa;margin-right:3px;vertical-align:-1px}
.support{left:470px;top:22px;width:128px;height:25px;background:#e6e6e6;border-radius:3px}
.support .icon{left:9px;top:5px}
.support .label{left:43px;top:3px;font-size:6.5px;color:#666}
.support .phone{left:42px;top:11px;font-family:"Lato",sans-serif;font-weight:700;font-size:10.5px;color:var(--blue)}

/* nav */
.mainnav{left:0;top:51px;width:690px;height:24px;background:linear-gradient(#2459b0,var(--blue-dark))}
.mainnav a{position:absolute;top:0;height:24px;line-height:24px;color:#fff;font-size:7.5px;font-weight:600;letter-spacing:.2px}
.mainnav a.active{background:linear-gradient(#3a93e0,var(--blue-light));text-align:center;width:54px}

/* hero */
.hero{left:0;top:75px;width:690px;height:215px;background:linear-gradient(100deg,var(--hero-a) 0%,#f4f6f9 40%,var(--hero-b) 100%)}
.product-name{left:93px;top:106px;font-family:"Lato",sans-serif;font-weight:700;font-size:22px;color:var(--blue);letter-spacing:-.3px}
.hero-copy{left:94px;top:148px;width:238px;font-size:8.3px;line-height:1.5;color:#333}
.btn{position:absolute;height:23px;border-radius:3px;color:#fff;font-family:"Lato",sans-serif;font-weight:700;font-size:10.5px;line-height:23px;padding-left:12px}
.btn .arrow{position:absolute;right:7px;top:5px;width:13px;height:13px;border-radius:50%;background:#fff}
.btn .arrow::after{content:"";position:absolute;left:4px;top:3.5px;border:3px solid transparent;border-left:5px solid currentColor}
.btn-orange{background:linear-gradient(#f7a13a,var(--orange-dark))}
.btn-orange .arrow{color:var(--orange-dark)}
.btn-blue{background:linear-gradient(#2f5fb4,var(--blue-dark))}
.btn-blue .arrow{color:var(--blue-dark)}
.dots{display:flex;gap:3px}
.dots i{width:5px;height:5px;border-radius:50%;background:#d3d7dd;display:block}
.dots i.on{background:var(--blue)}
.product-box{left:416px;top:86px;width:176px;height:246px;background:linear-gradient(90deg,#d9d9d9,#f4f4f4 40%,#cfcfcf 85%,#a9a9a9);border-radius:6px}
.proof{left:0;top:290px;width:690px;height:60px;background:#f1f3f6}
.proof p{position:absolute;left:92px;top:9px;font-size:12px;color:#555;font-family:"Open Sans",sans-serif;letter-spacing:-.1px}
.share{position:absolute;top:32px;height:10px;padding:0 4px;border:1px solid #c5ccd6;background:#eef2f7;border-radius:2px;font-size:6px;line-height:8px;color:#2d4d80}

/* welcome */
.photo{background:linear-gradient(#6f8aa8,#4a5a66)}
.welcome-text{font-size:6.9px;line-height:10.5px;letter-spacing:-.05px;color:var(--muted)}
.links{font-size:7.2px}
.pdf{display:inline-block;width:7px;height:8px;background:#c8302a;vertical-align:-1px;margin:0 4px 0 6px}
.video{left:457px;top:393px;width:142px;height:111px;background:linear-gradient(#1b3f8c,#0f2a63)}
.video .bar{position:absolute;left:0;bottom:0;width:100%;height:10px;background:#1a1a1a}
.video .play{position:absolute;left:59px;top:32px;width:24px;height:17px;background:rgba(0,0,0,.55);border-radius:3px}
.video .play::after{content:"";position:absolute;left:9px;top:4px;border:4.5px solid transparent;border-left:7px solid #fff}
.divider{left:92px;width:506px;height:6px;background:radial-gradient(ellipse at top,rgba(0,0,0,.09),rgba(0,0,0,0) 70%)}

/* services */
.service{position:absolute;top:597px;width:120px;text-align:center}
.service .ic{display:block;margin:0 auto;height:24px}
.service h3{font-family:"Lato",sans-serif;font-weight:400;font-size:11px;color:#222;margin-top:5px}
.service p{margin-top:16px;font-size:7.2px;line-height:11.8px;color:var(--muted)}
.more{position:absolute;top:775px;width:36px;height:12px;background:var(--blue);border-radius:2px;color:#fff;font-size:6.5px;line-height:12px;text-align:center;font-weight:600}

/* simulation */
.simulate{left:92px;top:811px;width:507px;height:56px;border:1px solid #e4e4e4;border-left:4px solid var(--orange);background:linear-gradient(#fff,#f5f5f5)}
.simulate h4{position:absolute;left:14px;top:9px;font-family:"Lato",sans-serif;font-weight:700;font-size:10.2px;color:#111;line-height:1.25}
.simulate em{position:absolute;left:14px;top:37px;font-size:6.6px;color:#888}

/* testimonials & partners */
.quote-box{left:92px;top:922px;width:245px;height:60px;background:#fff;border:1px solid #e6e6e6;box-shadow:0 2px 3px rgba(0,0,0,.08)}
.quote-box .qm{position:absolute;left:4px;top:-6px;font-family:Georgia,serif;font-size:30px;color:#d5d5d5}
.quote-box .logo-sq{position:absolute;left:24px;top:13px;width:24px;height:24px;background:#fff;border:1px solid #ddd}
.quote-box .logo-sq::after{content:"";position:absolute;left:5px;top:5px;width:12px;height:12px;background:#c0243c}
.quote-box p{position:absolute;left:58px;top:8px;width:180px;font-style:italic;font-size:6.9px;line-height:1.5;color:#555;text-align:center}
.author{left:122px;top:988px;font-size:6.8px;color:#555}
.author b{color:var(--blue);font-weight:600;font-style:italic}
.partner{position:absolute;width:68px;height:38px;border:1px solid #f3a662;background:#fff}
.partner i{position:absolute;left:14px;top:12px;width:38px;height:12px;background:#c7c7c7;border-radius:2px}
.partner.round i{left:21px;top:6px;width:24px;height:24px;border-radius:50%}

/* footer */
.footer{left:0;top:1037px;width:690px;height:163px;background:var(--footer)}
.footer h5{position:absolute;font-family:"Open Sans",sans-serif;font-weight:400;font-size:9.5px;color:#333}
.footer ul{position:absolute;list-style:none;font-size:7px;color:#666;line-height:13px}
.footer .plain{position:absolute;font-size:7px;color:#666;line-height:13px;white-space:nowrap}
.footer .plain.mail{font-size:6.4px;letter-spacing:-.1px}
.social{display:flex;gap:3px}
.social i{display:block;width:12px;height:12px;border-radius:2px;background:#3f73b8}
.social i.alt{background:#e48a2b}
.email{left:437px;top:1072px;width:146px;height:14px;border:1px solid #cfcfcf;background:#e4e4e4;font-size:6px;color:#999;padding:3px 5px}
.subscribe{left:523px;top:1116px;width:61px;height:12px;background:var(--blue);color:#fff;border-radius:2px;font-size:7px;line-height:12px;text-align:center}
.copyright{left:0;top:1180px;width:690px;text-align:center;font-size:7px;color:#555}
.foot-rule{left:85px;top:1170px;width:520px;height:1px;background:#dcdcdc}
</style>
</head>
<body>

<header class="header">
  <div class="abs brand"><span class="brand-mark"></span><span class="brand-name">TALMERO</span></div>
  <div class="abs toolbar"><span>Search</span><span>Special</span><span>Login</span></div>
  <div class="abs support">
    <svg class="abs icon" width="14" height="15" viewBox="0 0 14 15"><rect x="0" y="0" width="14" height="15" rx="2" fill="#9aa0a6"/><path d="M4 3c1 0 1.5 2 1 2.6-.4.4-.6.6 0 1.6s1.2 1.5 1.7 1.1c.6-.4 2.6.4 2.4 1.4-.2 1.2-1.8 1.6-3.2.6C3.8 8.9 2.5 6.4 3 4.2 3.2 3.5 3.5 3 4 3z" fill="#fff"/></svg>
    <span class="abs label">Call for Online Support</span>
    <span class="abs phone">0800 555.0142</span>
  </div>
</header>

<nav class="abs mainnav">
  <a class="active" style="left:92px">HOME</a>
  <a style="left:156px">ABOUT US</a>
  <a style="left:217px">PRODUCTS</a>
  <a style="left:280px">SOLUTIONS</a>
  <a style="left:346px">SERVICES</a>
  <a style="left:403px">PARTNERS PROGRAM</a>
  <a style="left:504px">CLIENTS</a>
  <a style="left:557px">CONTACTS</a>
</nav>

<section class="abs hero"></section>
<div class="abs product-name">brisk link</div>
<p class="abs hero-copy">Ligue sem limite a custo ZERO -entre filiais - e pague o custo de ligação local para ligações DDD. O BRISK link oferece recursos de integração entre PABX de outras filiais ou com operadoras VoIP para criação de Rotas de Menor Custo através de protocolo IAX, H323 ou SIP.</p>
<a class="btn btn-orange" style="left:92px;top:233px;width:101px">Learn More<span class="arrow"></span></a>
<a class="btn btn-blue" style="left:203px;top:233px;width:128px">Assemble Solution<span class="arrow"></span></a>
<div class="abs dots" style="left:98px;top:270px"><i class="on"></i><i></i><i></i><i></i><i></i></div>

<section class="abs proof">
  <p>Used by over 125,000 companies around the world.</p>
  <span class="share" style="left:92px">Post</span>
  <span class="share" style="left:126px">Like</span>
</section>
<div class="abs product-box" role="img" aria-label="Boxed product package for the BRISK link software"></div>

<h2 style="left:92px;top:363px">Welcome to Talmero</h2>
<div class="abs photo" style="left:94px;top:392px;width:116px;height:82px" role="img" aria-label="Talmero headquarters building with a car parked in front"></div>
<p class="abs welcome-text" style="left:216px;top:391px;width:226px">Lorem ipsum dolor sit amet, consectetuer adipiscing elit. Aenean commodo ligula eget dolor. Aenean massa. Cum sociis natoque penatibus et magnis dis parturient montes, nascetur ridiculus mus. Donec quam felis, ultricies nec, pellentesque eu, pretium quis, sem. Nulla consequat massa quis enim. Donec pede justo, fringilla vel, aliquet nec, vulputate eget, arcu. In enim justo, rhoncus ut, imperd a, venenatis vitae, justo. Nullam dictum felis eu pede mollis pretium. Integer tincidunt. Cras dapibus. Etiam rhoncus. Maecenas tempus,</p>
<p class="abs welcome-text" style="left:94px;top:477px;width:348px">Lorem ipsum dolor sit amet, consectetuer adipiscing elit. Aenean commodo ligula eget dolor. Aenean massa. Cum sociis natoque penatibus et magnis dis parturient montes, nascetur ridiculus mus. Donec quam felis, ultricies nec, pellentesque eu, pretium quis, sem. Nulla consequat massa quis enim.</p>
<div class="abs links" style="left:94px;top:519px"><a>Learn More »</a> <span style="color:#bbb;margin-left:6px">|</span><span class="pdf"></span><a>Download Whitepaper</a></div>

<h2 style="left:456px;top:363px">Learn More</h2>
<div class="abs video" role="img" aria-label="Training video with a Talmero presenter"><span class="play"></span><span class="bar"></span></div>
<a class="abs links" style="left:457px;top:519px">See All Training Videos »</a>
<div class="abs divider" style="top:545px"></div>

<h2 style="left:0;top:560px;width:690px;text-align:center">Our Services</h2>

<div class="service" style="left:89px">
  <svg class="ic" width="24" height="24" viewBox="0 0 24 24"><circle cx="12" cy="12" r="10" fill="#ddd" stroke="#777" stroke-width="1.5"/><circle cx="12" cy="12" r="4" fill="#777"/></svg>
  <h3>Our Service 1</h3>
  <p>Etiam rhoncus. Maecenas tempus, tellus eget condimentum rhoncus, sem quam semper libero, sit amet adipiscing sem neque sed ipsum. Nam quam nunc, blandit vel, luctus pulvinar, hendrerit id, lorem. Mae-cenas nec odio et ante tincidunt tempus. Donec vitae sapien ut libero venenatis faucibus.</p>
</div>
<div class="service" style="left:219px">
  <svg class="ic" width="24" height="24" viewBox="0 0 24 24"><rect x="2" y="7" width="20" height="15" rx="2" fill="#cfcfcf" stroke="#555" stroke-width="1.2"/><path d="M8 7V4h8v3" fill="none" stroke="#555" stroke-width="1.5"/></svg>
  <h3>Our Service 1</h3>
  <p>Etiam rhoncus. Maecenas tempus, tellus eget condimentum rhoncus, sem quam semper libero, sit amet adipiscing sem neque sed ipsum. Nam quam nunc, blandit vel, luctus pulvinar, hendrerit id, lorem. Mae-cenas nec odio et ante tincidunt tempus.</p>
</div>
<div class="service" style="left:348px">
  <svg class="ic" width="24" height="24" viewBox="0 0 24 24"><path d="M2 9c0-4 20-4 20 0v2h-5V9H7v2H2z" fill="#333"/><path d="M5 12h14l2 9H3z" fill="#444"/><circle cx="12" cy="16" r="3" fill="#999"/></svg>
  <h3>Our Service 1</h3>
  <p>Etiam rhoncus. Maecenas tempus, tellus eget condimentum rhoncus, sem quam semper libero, sit amet adipiscing sem neque sed ipsum. Nam quam nunc, blandit vel, luctus pulvinar, hendrerit id, lorem. Mae-cenas nec odio et ante tincidunt tempus. Donec vitae sapien ut libero venenatis faucibus ante.</p>
</div>
<div class="service" style="left:479px">
  <svg class="ic" width="24" height="24" viewBox="0 0 24 24"><path d="M4 20L20 4" stroke="#7a8ea8" stroke-width="4"/><rect x="14" y="3" width="7" height="7" fill="#4a9a4a"/><rect x="3" y="14" width="7" height="7" fill="#4a9a4a"/></svg>
  <h3>Our Service 1</h3>
  <p>Etiam rhoncus. Maecenas tempus, tellus eget condimentum rhoncus, sem quam semper libero, sit amet adipiscing sem neque sed ipsum. Nam quam nunc, blandit vel, luctus pulvinar, hendrerit id, lorem. Mae-cenas nec odio et ante tincidunt tempus.</p>
</div>
<a class="more" style="left:133px">more »</a>
<a class="more" style="left:262px">more »</a>
<a class="more" style="left:391px">more »</a>
<a class="more" style="left:521px">more »</a>

<section class="abs simulate">
  <h4>Do you want to make simulation for your phone consumption,<br>and see what we could save in terms of phone expenses</h4>
  <em>Horums ser quidem rerum facilis dolores nemis omnis fugats vitaes nemo minima rerums unsers sadips amets.</em>
</section>
<a class="btn btn-orange" style="left:462px;top:826px;width:119px">Make Simulation<span class="arrow"></span></a>

<h2 style="left:92px;top:899px;font-size:10.5px">Testimonials</h2>
<div class="abs quote-box">
  <span class="qm">“</span>
  <span class="logo-sq"></span>
  <p>If scientists want to send 400 files totaling about 13 GB for review, Corvane Delivery Server, which has terabytes of storage space, handles the load easily.... It is a beautiful and elegant tool anyone can use.</p>
</div>
<svg class="abs" style="left:100px;top:981px" width="20" height="10" viewBox="0 0 20 10"><path d="M0 0h20L0 10z" fill="#fff" stroke="#e6e6e6"/></svg>
<div class="abs author"><b>Owen Hale</b>, Director of Research Computing</div>
<div class="abs dots" style="left:303px;top:990px"><i class="on"></i><i></i><i></i><i></i></div>
<a class="abs" style="left:280px;top:1018px;font-size:7px">All testimonials »</a>

<h2 style="left:351px;top:899px;font-size:10.5px">Our Partners</h2>
<div class="partner" style="left:362px;top:922px"><i></i></div>
<div class="partner" style="left:440px;top:922px"><i></i></div>
<div class="partner" style="left:517px;top:922px"><i></i></div>
<div class="partner" style="left:362px;top:968px"><i></i></div>
<div class="partner" style="left:440px;top:968px"><i></i></div>
<div class="partner round" style="left:517px;top:968px"><i></i></div>
<a class="abs" style="left:555px;top:1018px;font-size:7px">All Partners »</a>

<footer class="abs footer">
  <h5 style="left:91px;top:12px">Navigation</h5>
  <ul style="left:93px;top:31px"><li>Home</li><li>Innovations</li><li>Solutions</li><li>Professionals</li><li>About Us</li><li>Join us</li></ul>
  <h5 style="left:195px;top:12px">Contact Us</h5>
  <div class="plain" style="left:197px;top:31px">Rua Serra Alta, 820<br>Bairro Vale Claro,<br>Porto Serrano – PS<br>CEP: 50990-210</div>
  <div class="plain" style="left:300px;top:31px">Phone<br>Fax:<br>Email</div>
  <div class="plain" style="left:328px;top:31px">: &nbsp;(83) 5550.0188<br>: &nbsp;(83) 5550.0199</div>
  <div class="plain mail" style="left:328px;top:57px">: &nbsp;<u>sac@talmero-example.com.br</u></div>
  <h5 style="left:195px;top:95px">Stay Connected</h5>
  <div class="abs social" style="left:281px;top:95px"><i></i><i></i><i></i><i class="alt"></i></div>
  <h5 style="left:437px;top:12px">Subscribe to Our Newsletter</h5>
  <div class="plain" style="left:437px;top:55px">We will never share your personal information</div>
</footer>
<svg class="abs" style="left:562px;top:1038px" width="38" height="22" viewBox="0 0 38 22"><path d="M2 4l34-2-6 18z" fill="#f7f7f7" stroke="#c9c9c9" stroke-dasharray="2 1.5"/></svg>
<div class="abs email">E-mail:</div>
<div class="abs subscribe">Subscribe</div>
<div class="abs foot-rule"></div>
<div class="abs copyright">© Talmero 2013. All Rights Reserved</div>

</body>
</html>
```